Lanterne architecture business cards

We are a new company based in New Zealand. We Specialize in High end Luxury Residential Architecture.

Every home is bespoke and is designed to each clients individual requirements and needs.

I like to design buildings that inspire people through light and form while offering a high level of comfort and usability.

Lines of sight, proportion and balance are fundamental to the spaces I create.
Updates

August 5th is current deadline - Today's date is the 13th of August.

Target Market(s)

New Zealanders who want a custom individual home design, typically 30-65 year old males and females

Industry/Entity Type

Architecture

Contact Information for Business Card

Director - Derek Tolson
Contact Number - 0279164073
Email - info@lanternearchitecture-example.co.nz
Webstie - www.lanternearchitecture-example.co.nz
Social Media - @lanternearchitecture

Font styles to use
Sans Serif

Requirements
Must have
• Logo (Both Sides)
Website
Email
Contact Number
Social Media

Nice to have
• Texture
Should not have
• More than 3 colours - typically I would've thought 2 would be good to match the logo.

```html
<!DOCTYPE html>
<html lang="en">
<head>
<meta charset="utf-8">
<title>Lanterne architecture business cards</title>
<link rel="stylesheet" href="https://fonts.googleapis.com/css2?family=Open+Sans:wght@300;400;700&display=swap">
<style>
  :root {
    --backdrop: #9a9a9a;
    --paper: #f4f4f2;
    --ink: #3a3a3a;
    --ink-soft: #6b6b6b;
    --card-black: #1f1f20;
    --pattern-dark: #181819;
    --pattern-light: #3a3a3c;
    --white: #ffffff;
  }
  * { margin: 0; padding: 0; box-sizing: border-box; }
  html, body { width: 1200px; height: 996px; overflow: hidden; }
  body {
    background: var(--backdrop);
    font-family: "Open Sans", sans-serif;
    position: relative;
  }
  .card {
    position: absolute;
    box-shadow: 0 18px 40px rgba(0,0,0,0.25);
  }

  /* Front: portrait */
  .card-front {
    left: 150px; top: 223px;
    width: 330px; height: 550px;
    background: var(--paper);
    color: var(--ink);
    text-align: center;
  }
  .brand {
    position: absolute; top: 70px; left: 0; right: 0;
    display: flex; flex-direction: column; align-items: center;
  }
  .brand-dot {
    width: 30px; height: 30px; border-radius: 50%;
    border: 3px solid var(--ink);
    margin-bottom: 22px;
  }
  .brand-name {
    font-weight: 300; font-size: 17px;
    letter-spacing: 0.32em; text-transform: uppercase;
    color: var(--ink); line-height: 1.5;
    padding-left: 0.32em;
  }
  .person { position: absolute; top: 218px; left: 0; right: 0; }
  .person-name {
    font-weight: 700; font-size: 17px;
    letter-spacing: 0.02em; text-transform: uppercase;
  }
  .person-role { font-weight: 400; font-size: 12px; color: var(--ink-soft); margin-top: 1px; }

  .icon-rule {
    position: absolute; top: 290px; left: 40px; right: 40px;
    display: flex; align-items: center; gap: 8px;
  }
  .icon-rule .rule { flex: 1; height: 1px; background: var(--ink); }
  .icon-rule svg { width: 18px; height: 18px; flex: none; }

  .contact {
    position: absolute; top: 322px; left: 0; right: 0;
    font-weight: 300; font-size: 12.5px; line-height: 1.55;
    color: var(--ink);
  }
  .dash {
    position: absolute; top: 430px; left: 155px;
    width: 20px; height: 2px; background: var(--ink);
  }
  .social {
    position: absolute; top: 460px; left: 0; right: 0;
    display: flex; justify-content: center; align-items: center; gap: 8px;
    font-weight: 300; font-size: 12.5px;
  }
  .social-dot { width: 9px; height: 9px; border-radius: 50%; background: var(--ink); }

  /* Back: landscape */
  .card-back {
    left: 530px; top: 333px;
    width: 550px; height: 330px;
    background: var(--card-black);
    overflow: hidden;
  }
  .back-pattern {
    position: absolute; inset: 0;
    background: linear-gradient(120deg, var(--pattern-dark) 0%, var(--card-black) 50%, var(--pattern-light) 100%);
  }
  .back-brand {
    position: absolute; left: 70px; top: 150px;
    display: flex; align-items: center; gap: 12px;
    color: var(--white);
    font-weight: 400; font-size: 18px;
    letter-spacing: 0.2em; text-transform: uppercase;
  }
  .back-brand .brand-dot-white {
    width: 14px; height: 14px; border-radius: 50%; background: var(--white);
  }
</style>
</head>
<body>

  <section class="card card-front">
    <div class="brand">
      <div class="brand-dot"></div>
      <div class="brand-name">Lanterne<br>architecture</div>
    </div>

    <div class="person">
      <div class="person-name">Derek Tolson</div>
      <div class="person-role">Director</div>
    </div>

    <div class="icon-rule">
      <span class="rule"></span>
      <svg viewBox="0 0 18 18" aria-label="phone"><circle cx="9" cy="9" r="8" fill="none" stroke="#3a3a3a" stroke-width="1.2"/><path d="M6 5.5l1.6-.5 1 2-1 .8c.5 1.2 1.2 1.9 2.4 2.4l.8-1 2 1-.5 1.6c-3.3.2-6.5-3-6.3-6.3z" fill="#3a3a3a"/></svg>
      <svg viewBox="0 0 18 18" aria-label="email"><circle cx="9" cy="9" r="8" fill="none" stroke="#3a3a3a" stroke-width="1.2"/><rect x="5" y="6" width="8" height="6" fill="none" stroke="#3a3a3a" stroke-width="1"/><path d="M5 6l4 3.2L13 6" fill="none" stroke="#3a3a3a" stroke-width="1"/></svg>
      <svg viewBox="0 0 18 18" aria-label="website"><circle cx="9" cy="9" r="8" fill="none" stroke="#3a3a3a" stroke-width="1.2"/><circle cx="9" cy="9" r="4.5" fill="none" stroke="#3a3a3a" stroke-width="1"/><path d="M4.5 9h9M9 4.5c-2 2.5-2 6.5 0 9M9 4.5c2 2.5 2 6.5 0 9" fill="none" stroke="#3a3a3a" stroke-width="0.9"/></svg>
      <span class="rule"></span>
    </div>

    <div class="contact">
      <div>027 916 4073</div>
      <div>info@lanternearchitecture-example.co.nz</div>
      <div>www.lanternearchitecture-example.co.nz</div>
    </div>

    <div class="dash"></div>

    <div class="social">
      <span class="social-dot"></span>
      <span>@lanternearchitecture</span>
    </div>
  </section>

  <section class="card card-back">
    <div class="back-pattern" role="img" aria-label="Tonal repeat pattern of the brand mark across the dark card"></div>
    <div class="back-brand">
      <span class="brand-dot-white"></span>
      <span>Lanterne</span>
    </div>
  </section>

</body>
</html>
```